App for Lawyers & Accountants needs 'Professional' Styling

We want to style our app to convey a 'Professional' appearance. It's used by Lawyers, Accountants, Doctors etc. who take their work very seriously.

We currently trying to follow corvane layout guidelines, but we find our app looks very bland. I've uploaded a screenshot of our current app, and two mock-ups of more stylized versions, but we're not happy with those mock-ups.

We'd like to see alternate designs for those two mock-ups, that look much more professional.

The specific elements we'd like to improve/focus on are:
* Colour of the top and left nav bars
* Appearance of the left nav, size, icons spacing
* Appearance of the buttons on the top right, so the user knows they are buttons they can press
* Spacing of the dashboard, background colour and spacing, colour/layout of the 'overdue' and 'todo' accordion headings in the 'my tasks' section.
* List view background grey, to be consistent with dashboard, but unobtrusive
* List view tabs to be obvious as tabs, but 'saved searches', filters and the export icon to still be associated with the data displayed, but it should be obvious to the user that those are different buttons, not just more tabs. (I.e. the filters button opens a panel below it that allows the user to filter the data in the list.)
* General appearance of the popup menu when you push the 'add' button on the top right

However, despite those specifics I'm sure it's all the subtle elements of the design that make a big difference.

Our brand colour is 1D4F91, and we use A20067 as a secondary colour in print media, (although it doesn't seem to work to well within the app.) Our brand font is signika. We'd like the designs to be based on those colours & font.

Professional people, Lawyers, Accountants, Doctors etc.

Sans Serif
• Signika

0255a3

• The most 'Professional' experience/quality possible. Think the quality & brand image of brindlewave desk, but taken to a higher level.
• An example/mock-up of the dashboard, list view and 'add' item popup menu
• Display the dashboard cards with the same information as our mock-ups - the information there is important and we don't have any extra cards to add (in the near term)
• Various colour combinations for the top and left nav bars, based on our primary blue brand colour, and perhaps some shade of dark grey.

```html
<!DOCTYPE html>
<html lang="en">
<head>
<meta charset="utf-8">
<title>AppName – Professional Styling</title>
<link rel="stylesheet" href="https://fonts.googleapis.com/css2?family=Signika:wght@300;400;600&display=swap">
<style>
:root{
  --brand:#1d4f91;
  --brand-dark:#17427c;
  --accent:#a20067;
  --bg:#f2f3f6;
  --card:#ffffff;
  --text:#2d2f36;
  --muted:#8a8f9a;
  --line:#e3e5ea;
  --icon:#9aa3b5;
  --chip:#eef0f4;
}
*{box-sizing:border-box;margin:0;padding:0}
html,body{width:1200px;height:1200px;overflow:hidden}
body{font-family:'Signika',sans-serif;color:var(--text);
  background:
    linear-gradient(135deg,transparent 0 58%,rgba(40,20,40,.55) 58% 63%,transparent 63%),
    linear-gradient(135deg,#8b5a79 0%,#9a3d78 45%,#a22e76 100%);}
.stage{position:absolute;left:0;top:0;width:1500px;height:1500px;transform:scale(.8);transform-origin:0 0}
.window{position:absolute;width:1120px;height:630px;background:var(--bg);border-radius:10px;overflow:hidden;box-shadow:0 18px 40px rgba(20,10,40,.35)}
.w-list{left:40px;top:40px}
.w-add{left:190px;top:376px}
.w-dash{left:340px;top:831px}

/* sidebar */
.sidebar{position:absolute;left:0;top:0;width:198px;height:100%;background:var(--brand);color:#fff}
.brandrow{position:absolute;left:14px;top:15px;display:flex;align-items:center;gap:12px}
.burger{width:16px;height:12px;border-top:2px solid #fff;border-bottom:2px solid #fff;position:relative}
.burger::after{content:"";position:absolute;left:0;top:3px;width:16px;height:2px;background:#fff}
.brand-dot{width:30px;height:30px;border-radius:50%;background:#fff;margin-left:6px}
.brand-name{font-size:16px;font-weight:600;letter-spacing:.2px}
.add-btn{position:absolute;left:23px;top:73px;width:140px;height:34px;border-radius:17px;background:#fff;color:var(--accent);font-size:12px;font-weight:600;display:flex;align-items:center;justify-content:center;gap:30px;box-shadow:0 3px 8px rgba(0,0,0,.2)}
.add-btn b{font-size:20px;font-weight:600;line-height:1}
.nav{position:absolute;left:0;top:138px;width:100%;list-style:none}
.nav li{height:41px;display:flex;align-items:center;padding-left:20px;gap:17px;font-size:11px;color:#b7c6de;position:relative}
.nav li.active{color:#fff;font-weight:600}
.nav li.active::before{content:"";position:absolute;left:0;top:9px;width:3px;height:23px;background:#fff}
.nav svg{width:16px;height:16px;fill:currentColor}
.nav .badge{position:absolute;right:16px;width:18px;height:18px;border-radius:50%;background:#fff;color:var(--accent);font-size:8px;display:flex;align-items:center;justify-content:center}
.settings{position:absolute;left:20px;bottom:16px;display:flex;align-items:center;gap:17px;font-size:11px;color:#c8d4e6}
.settings svg{width:16px;height:16px;fill:currentColor}

/* top bar */
.topbar{position:absolute;left:198px;top:0;right:0;height:58px}
.search{position:absolute;left:18px;top:14px;width:407px;height:30px;background:#e8e9ee;border-radius:4px;font-size:10.5px;color:var(--muted);padding:9px 16px}
.search svg{position:absolute;right:10px;top:10px;width:10px;height:10px}
.top-icon{position:absolute;top:20px;width:18px;height:18px;fill:#6b7080}
.avatar{position:absolute;left:794px;top:16px;width:24px;height:24px;border-radius:50%;background:linear-gradient(#c98d66,#7a4b3a)}
.user{position:absolute;left:828px;top:22px;font-size:11px;color:var(--text)}
.caret{position:absolute;left:893px;top:24px;width:6px;height:6px;border-right:1.3px solid #666;border-bottom:1.3px solid #666;transform:rotate(45deg)}

/* dashboard */
.sec-title{position:absolute;font-size:15px;font-weight:400;color:var(--text)}
.card{position:absolute;background:var(--card);border-radius:3px;box-shadow:0 1px 3px rgba(0,0,0,.05)}
.tabs2{position:absolute;left:0;top:0;width:100%;height:40px}
.tabs2 span{position:absolute;top:10px;font-size:9px;color:#555;letter-spacing:.2px}
.tabs2 .on{color:var(--accent);font-weight:600}
.tabs2 .bar{position:absolute;left:170px;top:33px;width:81px;height:2px;background:var(--accent)}
.task{position:absolute;left:12px;width:256px;height:40px}
.task .rad{position:absolute;left:0;top:1px;width:12px;height:12px;border:1.3px solid #777;border-radius:50%}
.task .rad.done{background:var(--accent);border-color:var(--accent)}
.task .rad.done::after{content:"";position:absolute;left:3px;top:1.5px;width:3px;height:5px;border-right:1.5px solid #fff;border-bottom:1.5px solid #fff;transform:rotate(45deg)}
.task .t{position:absolute;left:22px;top:0;font-size:10.5px;color:var(--text)}
.task .t.s{font-size:9px}
.task .sub{position:absolute;left:24px;top:16px;font-size:8.5px;color:#666;display:flex;align-items:center;gap:7px}
.task .d{position:absolute;right:0;top:1px;font-size:8.5px;color:var(--muted)}
.bc{width:9px;height:6px;background:#9aa0ab;border-radius:1px;display:inline-block}
.stat{position:absolute;top:14px;text-align:center;width:90px}
.stat small{display:block;font-size:7px;color:#777;letter-spacing:.3px}
.stat strong{display:block;font-size:13px;font-weight:400;margin-top:4px}
.stat.on small,.stat.on strong{color:var(--accent)}
.stat.on::after{content:"";position:absolute;left:16px;top:44px;width:58px;height:2px;background:var(--accent)}
.chart{position:absolute;left:0;top:56px}
.legend{position:absolute;top:218px;font-size:8.5px;color:#444;display:flex;align-items:center;gap:10px}
.legend i{width:11px;height:11px;border-radius:50%;display:inline-block}
.matter{position:absolute;left:12px;width:256px;height:40px}
.matter .ic{position:absolute;left:0;top:0;width:30px;height:30px;border-radius:50%;background:var(--chip)}
.matter .ic::after{content:"";position:absolute;left:9px;top:11px;width:12px;height:8px;background:var(--accent);border-radius:1px}
.matter p{position:absolute;left:39px;top:0;width:172px;font-size:8.5px;line-height:13px;color:var(--text)}
.matter .d{position:absolute;right:0;top:0;font-size:8px;color:var(--muted)}
.doc{position:absolute;left:12px;width:256px;height:20px;font-size:8.5px;display:flex;align-items:center;gap:14px}
.doc .fi{width:13px;height:14px;border-radius:2px}
.doc .d{position:absolute;right:0;color:var(--muted);font-size:8px}
.fi.w{background:#2b5fb0}.fi.x{background:#1f8a4c}.fi.p{background:#d8512c}

/* add popup */
.popup{position:absolute;left:17px;top:73px;width:175px;height:233px;background:#fff;color:var(--text);border-radius:2px;box-shadow:0 6px 18px rgba(0,0,0,.25);padding:14px 16px}
.popup h3{font-size:12px;font-weight:400;color:var(--text);margin-bottom:10px}
.popup ul{list-style:none}
.popup li{height:29.4px;display:flex;align-items:center;justify-content:space-between;font-size:10.5px;color:var(--text)}
.popup svg{width:12px;height:12px;fill:var(--brand)}
.sel-line{position:absolute;left:0;top:136px;width:2px;height:24px;background:#fff}

/* list view */
.page-title{position:absolute;left:218px;top:67px;font-size:15px;font-weight:400}
.filter-btn{position:absolute;left:1020px;top:62px;width:82px;height:27px;background:#fff;border-radius:2px;box-shadow:0 1px 4px rgba(0,0,0,.12);color:var(--accent);font-size:9.5px;display:flex;align-items:center;justify-content:center;gap:10px}
.filter-btn svg{width:14px;height:12px;fill:var(--accent)}
.list-card{position:absolute;left:218px;top:96px;width:884px;height:260px;background:#fff}
.ltabs{position:absolute;left:9px;top:0;width:864px;height:38px;border-bottom:1px solid var(--line);font-size:9.5px}
.ltabs .tab{position:absolute;top:16px}
.ltabs .tab.on{color:var(--accent);font-weight:600}
.ltabs .ul{position:absolute;left:0;top:36px;width:50px;height:2px;background:var(--accent)}
.tools{position:absolute;right:10px;top:11px;display:flex;align-items:center;gap:8px;font-size:9px;color:#444}
.tools .pp{border:1px solid #8aa0c4;color:var(--brand);padding:3px 5px;font-size:9px;border-radius:2px}
.tools svg{width:12px;height:12px;fill:#555}
.tools .gap{width:14px}
table{position:absolute;left:32px;top:52px;border-collapse:collapse;font-size:9px}
th{font-weight:400;color:#555;text-align:left;height:30px}
td{height:29px}
td.c{color:var(--brand)}
td.g{color:#555}
</style>
</head>
<body>
<div class="stage">

<!-- ===== List view ===== -->
<section class="window w-list">
  <aside class="sidebar">
    <div class="brandrow"><span class="burger"></span><span class="brand-dot"></span><span class="brand-name">AppName</span></div>
    <div class="add-btn"><b>+</b>ADD</div>
    <ul class="nav">
      <li><svg viewBox="0 0 16 16"><circle cx="8" cy="8" r="7"/></svg>Dashboard</li>
      <li class="active"><svg viewBox="0 0 16 16"><rect x="1" y="4" width="14" height="10" rx="1"/><rect x="5" y="1.5" width="6" height="3" rx="1"/></svg>My Matters</li>
      <li><svg viewBox="0 0 16 16"><circle cx="8" cy="5" r="3.5"/><path d="M1 15c0-4 3-6 7-6s7 2 7 6z"/></svg>Contacts</li>
      <li><svg viewBox="0 0 16 16"><path d="M3 13l4-8 6-3-3 6z"/></svg>Tasks<span class="badge">24</span></li>
      <li><svg viewBox="0 0 16 16"><path d="M10 2a3 3 0 014 4l-7 7a2 2 0 01-3-3l6-6 1 1-6 6a.6.6 0 001 1l7-7a1.6 1.6 0 00-2-2L4 10 3 9z"/></svg>Documents</li>
      <li><svg viewBox="0 0 16 16"><path d="M8 1a7 7 0 11-7 7h2a5 5 0 105-5zM7 4h2v4l3 2-1 1.5-4-2.5z"/></svg>Time Records</li>
    </ul>
  </aside>
  <header class="topbar">
    <div class="search">Search everything<svg viewBox="0 0 10 10"><circle cx="4" cy="4" r="3" fill="none" stroke="#666"/><path d="M6 6l3 3" stroke="#666"/></svg></div>
    <svg class="top-icon" style="left:708px" viewBox="0 0 16 16"><path d="M8 1a7 7 0 11-7 7h2a5 5 0 105-5zM7 4h2v4l3 2-1 1.5-4-2.5z"/></svg>
    <svg class="top-icon" style="left:748px" viewBox="0 0 16 16"><path d="M3 13l4-8 6-3-3 6z"/></svg>
    <span class="avatar" role="img" aria-label="User profile photo"></span><span class="user">Dana R.</span><span class="caret"></span>
  </header>
  <h1 class="page-title">My Matters</h1>
  <div class="filter-btn"><svg viewBox="0 0 14 12"><rect y="0" width="14" height="2"/><rect x="3" y="5" width="8" height="2"/><rect x="5" y="10" width="4" height="2"/></svg>Filter</div>
  <div class="list-card">
    <div class="ltabs">
      <span class="tab on" style="left:10px">ALL</span><span class="tab" style="left:53px">RECENT</span><span class="ul"></span>
      <div class="tools"><span class="pp">20 ⌄</span>Per Page<span class="gap"></span><svg viewBox="0 0 12 12"><rect width="12" height="12" rx="1"/></svg>Saved Searches<span class="gap"></span><svg viewBox="0 0 12 12"><path d="M0 0h8v4h4v8H0z"/></svg>Export</div>
    </div>
    <table>
      <colgroup><col style="width:341px"><col style="width:165px"><col style="width:134px"><col style="width:106px"><col style="width:100px"></colgroup>
      <tr><th>Title</th><th>Client</th><th>Practice Area</th><th>Column 4</th><th>Last Updated</th></tr>
      <tr><td>Abbott v. Moore Concerning Sale #707</td><td class="c">T Gorman</td><td class="g">Conveyancing</td><td class="g">Investment</td><td class="g">30 Jun 2017</td></tr>
      <tr><td>Abernathy v. Director of Prosecutions con Deceased #310</td><td class="c">Halvorsen Inc</td><td class="g">Estates</td><td class="g">Settlement</td><td class="g">16 Apr 2018</td></tr>
      <tr><td>Abernathy v. Director of Prosecutions con Investment #578</td><td class="c">Pryce &amp; Dunn</td><td class="g">Property</td><td class="g">Investment</td><td class="g">5 Mar 2018</td></tr>
      <tr><td>Abernathy v. Director of Prosecutions con Work Cover #295</td><td class="c">Keller Ostrom</td><td class="g">Personal Injury</td><td class="g">Signup</td><td class="g">2 Sep 2017</td></tr>
      <tr><td>Abernathy v. Schmitt Concerning Retail Lease #668</td><td class="c">Varga &amp; Holt</td><td class="g">Property</td><td class="g">Settlement</td><td class="g">28 Dec 2018</td></tr>
      <tr><td>Boston v. Moore Concerning Sale #501</td><td class="c">L Whitcombe</td><td class="g">Conveyancing</td><td class="g">Investment</td><td class="g">30 Jun 2017</td></tr>
    </table>
  </div>
</section>

<!-- ===== Dashboard with Add menu ===== -->
<section class="window w-add">
  <aside class="sidebar">
    <div class="brandrow"><span class="burger"></span><span class="brand-dot"></span><span class="brand-name">AppName</span></div>
    <span class="sel-line"></span>
    <ul class="nav" style="top:292px">
      <li><svg viewBox="0 0 16 16"><path d="M10 2a3 3 0 014 4l-7 7a2 2 0 01-3-3l6-6 1 1-6 6a.6.6 0 001 1l7-7a1.6 1.6 0 00-2-2L4 10 3 9z"/></svg>Documents</li>
      <li><svg viewBox="0 0 16 16"><path d="M8 1a7 7 0 11-7 7h2a5 5 0 105-5zM7 4h2v4l3 2-1 1.5-4-2.5z"/></svg>Time Records</li>
    </ul>
    <div class="settings"><svg viewBox="0 0 16 16"><circle cx="8" cy="8" r="6"/></svg>Settings</div>
    <div class="popup">
      <h3>Add</h3>
      <ul>
        <li>Time<svg viewBox="0 0 16 16"><path d="M8 1a7 7 0 11-7 7h2a5 5 0 105-5zM7 4h2v4l3 2-1 1.5-4-2.5z"/></svg></li>
        <li>Document<svg viewBox="0 0 16 16"><path d="M10 2a3 3 0 014 4l-7 7a2 2 0 01-3-3l6-6 1 1-6 6a.6.6 0 001 1l7-7a1.6 1.6 0 00-2-2L4 10 3 9z"/></svg></li>
        <li>Task<svg viewBox="0 0 16 16"><path d="M3 13l4-8 6-3-3 6z"/></svg></li>
        <li>Notes<svg viewBox="0 0 16 16"><path d="M2 2h12v12H2zM4 4v8h8V4zM5 6h6v1H5zm0 3h4v1H5z"/></svg></li>
        <li>Matter<svg viewBox="0 0 16 16"><rect x="1" y="4" width="14" height="10" rx="1"/><rect x="5" y="1.5" width="6" height="3" rx="1"/></svg></li>
        <li>Contact<svg viewBox="0 0 16 16"><circle cx="8" cy="5" r="3.5"/><path d="M1 15c0-4 3-6 7-6s7 2 7 6z"/></svg></li>
      </ul>
    </div>
  </aside>
  <header class="topbar">
    <div class="search">Search everything<svg viewBox="0 0 10 10"><circle cx="4" cy="4" r="3" fill="none" stroke="#666"/><path d="M6 6l3 3" stroke="#666"/></svg></div>
    <svg class="top-icon" style="left:708px" viewBox="0 0 16 16"><path d="M8 1a7 7 0 11-7 7h2a5 5 0 105-5zM7 4h2v4l3 2-1 1.5-4-2.5z"/></svg>
    <svg class="top-icon" style="left:748px" viewBox="0 0 16 16"><path d="M3 13l4-8 6-3-3 6z"/></svg>
    <span class="avatar" role="img" aria-label="User profile photo"></span><span class="user">Dana R.</span><span class="caret"></span>
  </header>
  <h2 class="sec-title" style="left:218px;top:67px">Tasks</h2>
  <h2 class="sec-title" style="left:521px;top:67px">Time Records</h2>
  <h2 class="sec-title" style="left:824px;top:67px">Recent Matters</h2>
  <div class="card" style="left:216px;top:100px;width:280px;height:520px">
    <div class="tabs2"><span style="left:41px">OVERDUE (4)</span><span class="on" style="left:186px">TO DO (20)</span><span class="bar"></span></div>
    <div class="task" style="top:52px"><span class="rad done"></span><span class="t s">Finalise Court Documents</span><span class="sub"><i class="bc"></i>1157 Ecerich v. The State of...</span><span class="d">Today</span></div>
    <div class="task" style="top:98px"><span class="rad"></span><span class="t">Task #2</span><span class="sub"><i class="bc"></i>Owen Marsh</span><span class="d">Tomorrow</span></div>
    <div class="task" style="top:145px"><span class="rad"></span><span class="t">Finalise Court Settlement Figures</span><span class="sub"><i class="bc"></i>1302 Pueblo de Oro v. The State of...</span><span class="d">15 May 2018</span></div>
    <div class="task" style="top:192px"><span class="rad"></span><span class="t">This is my 4th task</span><span class="sub"><i class="bc"></i>Short meeting with Ivo Brandt</span><span class="d">18 May 2018</span></div>
    <div class="task" style="top:238px"><span class="rad"></span><span class="t">No. 5 task</span><span class="sub"><i class="bc"></i>Report to Northgate HQ</span><span class="d">22 May 2018</span></div>
    <div class="task" style="top:285px"><span class="rad"></span><span class="t">Finalise Court Documents</span><span class="sub"><i class="bc"></i>1157 Ecerich v. The State of...</span><span class="d">26 May 2018</span></div>
    <div class="task" style="top:331px"><span class="rad"></span><span class="t">Task #7</span><span class="sub"><i class="bc"></i>Owen Marsh</span><span class="d">27 May 2018</span></div>
  </div>
  <div class="card" style="left:519px;top:100px;width:280px;height:244px">
    <div class="stat" style="left:2px"><small>TODAY</small><strong>5h 2m</strong></div>
    <div class="stat on" style="left:95px"><small>THIS WEEK</small><strong>24h 7m</strong></div>
    <div class="stat" style="left:188px"><small>THIS MONTH</small><strong>56h 34m</strong></div>
    <svg class="chart" width="280" height="150" viewBox="0 0 280 150">
      <rect x="0" y="40" width="280" height="110" fill="#eef0f4"/>
      <path d="M0 82 C60 70 100 30 160 32 S220 70 280 45 V102 H0Z" fill="#c7d0e0"/>
      <g font-size="8" fill="#444" font-family="Signika,sans-serif"><text x="10" y="10">10h</text><text x="10" y="33">8h</text><text x="10" y="56">6h</text><text x="10" y="79">4h</text><text x="10" y="102">2h</text></g>
      <path d="M0 104 C40 90 60 45 90 40 S150 92 190 82 S240 55 258 45 L280 38" fill="none" stroke="#a20067" stroke-width="1.4"/>
      <circle cx="258" cy="45" r="4.5" fill="#fff" stroke="#a20067" stroke-width="1.4"/>
      <g font-size="6.5" fill="#1d4f91" text-anchor="middle" font-family="Signika,sans-serif"><text x="44" y="116">S</text><text x="80" y="116">M</text><text x="116" y="116">T</text><text x="152" y="116">W</text><text x="188" y="116">T</text><text x="224" y="116">F</text><text x="259" y="116">S</text></g>
      <g font-size="8" fill="#333" text-anchor="middle" font-family="Signika,sans-serif"><text x="44" y="135">6</text><text x="80" y="135">7</text><text x="116" y="135">8</text><text x="152" y="135">9</text><text x="188" y="135">10</text><text x="224" y="135">11</text><text x="259" y="135">12</text></g>
    </svg>
    <div class="legend" style="left:43px"><i style="background:#b5c0d4"></i>Last Week</div>
    <div class="legend" style="left:174px"><i style="background:var(--accent)"></i>Last Week</div>
  </div>
  <h2 class="sec-title" style="left:521px;top:370px">Recent Documents</h2>
  <div class="card" style="left:519px;top:400px;width:280px;height:120px">
    <div class="doc" style="top:10px"><i class="fi w"></i>Court Doc101.docx<span class="d">1h</span></div>
    <div class="doc" style="top:45px"><i class="fi x"></i>Settlement Figures_Rk-Alder.xlsx<span class="d">4h</span></div>
  </div>
  <div class="card" style="left:822px;top:100px;width:278px;height:520px">
    <div class="matter" style="top:16px"><span class="ic"></span><p>1157 Abbott v. Director of Public Persecutions concerning motor vehicle</p><span class="d">2h</span></div>
    <div class="matter" style="top:69px"><span class="ic"></span><p>The generated Lorem Ipsum is therefore always free from repetition</p><span class="d">5h</span></div>
    <div class="matter" style="top:121px"><span class="ic"></span><p style="top:8px">1024 Lorem Ipsum is not simply random text.</p><span class="d" style="top:8px">12h</span></div>
    <div class="matter" style="top:174px"><span class="ic"></span><p>Peter Vance, a Latin professor at Elmwood College in Ohio</p><span class="d">20h</span></div>
    <div class="matter" style="top:226px"><span class="ic"></span><p>The standard chunk of Lorem Ipsum used since the 1500s</p><span class="d">1d</span></div>
    <div class="matter" style="top:279px"><span class="ic"></span><p>1157 Abbott v. Director of Public Persecutions concerning motor vehicle</p><span class="d">2d</span></div>
    <div class="matter" style="top:331px"><span class="ic"></span><p>The generated Lorem Ipsum is therefore always free from repetition</p><span class="d">5d</span></div>
  </div>
</section>

<!-- ===== Dashboard ===== -->
<section class="window w-dash">
  <aside class="sidebar">
    <div class="brandrow"><span class="burger"></span><span class="brand-dot"></span><span class="brand-name">AppName</span></div>
    <div class="add-btn"><b>+</b>ADD</div>
    <ul class="nav">
      <li class="active"><svg viewBox="0 0 16 16"><circle cx="8" cy="8" r="7"/></svg>Dashboard</li>
      <li><svg viewBox="0 0 16 16"><rect x="1" y="4" width="14" height="10" rx="1"/><rect x="5" y="1.5" width="6" height="3" rx="1"/></svg>My Matters</li>
      <li><svg viewBox="0 0 16 16"><circle cx="8" cy="5" r="3.5"/><path d="M1 15c0-4 3-6 7-6s7 2 7 6z"/></svg>Contacts</li>
      <li><svg viewBox="0 0 16 16"><path d="M3 13l4-8 6-3-3 6z"/></svg>Tasks<span class="badge">24</span></li>
      <li><svg viewBox="0 0 16 16"><path d="M10 2a3 3 0 014 4l-7 7a2 2 0 01-3-3l6-6 1 1-6 6a.6.6 0 001 1l7-7a1.6 1.6 0 00-2-2L4 10 3 9z"/></svg>Documents</li>
      <li><svg viewBox="0 0 16 16"><path d="M8 1a7 7 0 11-7 7h2a5 5 0 105-5zM7 4h2v4l3 2-1 1.5-4-2.5z"/></svg>Time Records</li>
    </ul>
    <div class="settings"><svg viewBox="0 0 16 16"><circle cx="8" cy="8" r="6"/></svg>Settings</div>
  </aside>
  <header class="topbar">
    <div class="search">Search everything<svg viewBox="0 0 10 10"><circle cx="4" cy="4" r="3" fill="none" stroke="#666"/><path d="M6 6l3 3" stroke="#666"/></svg></div>
    <svg class="top-icon" style="left:708px" viewBox="0 0 16 16"><path d="M8 1a7 7 0 11-7 7h2a5 5 0 105-5zM7 4h2v4l3 2-1 1.5-4-2.5z"/></svg>
    <svg class="top-icon" style="left:748px" viewBox="0 0 16 16"><path d="M3 13l4-8 6-3-3 6z"/></svg>
    <span class="avatar" role="img" aria-label="User profile photo"></span><span class="user">Dana R.</span><span class="caret"></span>
  </header>
  <h2 class="sec-title" style="left:218px;top:67px">Tasks</h2>
  <h2 class="sec-title" style="left:521px;top:67px">Time Records</h2>
  <h2 class="sec-title" style="left:824px;top:67px">Recent Matters</h2>
  <div class="card" style="left:216px;top:100px;width:280px;height:512px">
    <div class="tabs2"><span style="left:41px">OVERDUE (4)</span><span class="on" style="left:186px">TO DO (20)</span><span class="bar"></span></div>
    <div class="task" style="top:52px"><span class="rad done"></span><span class="t s">Finalise Court Documents</span><span class="sub"><i class="bc"></i>1157 Ecerich v. The State of...</span><span class="d">Today</span></div>
    <div class="task" style="top:98px"><span class="rad"></span><span class="t">Task #2</span><span class="sub"><i class="bc"></i>Owen Marsh</span><span class="d">Tomorrow</span></div>
    <div class="task" style="top:145px"><span class="rad"></span><span class="t">Finalise Court Settlement Figures</span><span class="sub"><i class="bc"></i>1302 Pueblo de Oro v. The State of...</span><span class="d">15 May 2018</span></div>
    <div class="task" style="top:192px"><span class="rad"></span><span class="t">This is my 4th task</span><span class="sub"><i class="bc"></i>Short meeting with Ivo Brandt</span><span class="d">18 May 2018</span></div>
    <div class="task" style="top:238px"><span class="rad"></span><span class="t">No. 5 task</span><span class="sub"><i class="bc"></i>Report to Northgate HQ</span><span class="d">22 May 2018</span></div>
    <div class="task" style="top:285px"><span class="rad"></span><span class="t">Finalise Court Documents</span><span class="sub"><i class="bc"></i>1157 Ecerich v. The State of...</span><span class="d">26 May 2018</span></div>
    <div class="task" style="top:331px"><span class="rad"></span><span class="t">Task #7</span><span class="sub"><i class="bc"></i>Owen Marsh</span><span class="d">27 May 2018</span></div>
    <div class="task" style="top:378px"><span class="rad"></span><span class="t">Finalise Court Settlement Figures</span><span class="sub"><i class="bc"></i>1302 Pueblo de Oro v. The State of...</span><span class="d">1 Jun 2018</span></div>
    <div class="task" style="top:424px"><span class="rad"></span><span class="t">This is my 9th task</span><span class="sub"><i class="bc"></i>Short meeting with Ivo Brandt</span><span class="d">16 Jun 2018</span></div>
    <div class="task" style="top:471px"><span class="rad"></span><span class="t">No. 10 task</span><span class="sub"><i class="bc"></i>Report to Northgate HQ</span><span class="d">4 Jul 2018</span></div>
  </div>
  <div class="card" style="left:519px;top:100px;width:280px;height:244px">
    <div class="stat" style="left:2px"><small>TODAY</small><strong>5h 2m</strong></div>
    <div class="stat on" style="left:95px"><small>THIS WEEK</small><strong>24h 7m</strong></div>
    <div class="stat" style="left:188px"><small>THIS MONTH</small><strong>56h 34m</strong></div>
    <svg class="chart" width="280" height="150" viewBox="0 0 280 150">
      <rect x="0" y="40" width="280" height="110" fill="#eef0f4"/>
      <path d="M0 82 C60 70 100 30 160 32 S220 70 280 45 V102 H0Z" fill="#c7d0e0"/>
      <g font-size="8" fill="#444" font-family="Signika,sans-serif"><text x="10" y="10">10h</text><text x="10" y="33">8h</text><text x="10" y="56">6h</text><text x="10" y="79">4h</text><text x="10" y="102">2h</text></g>
      <path d="M0 104 C40 90 60 45 90 40 S150 92 190 82 S240 55 258 45 L280 38" fill="none" stroke="#a20067" stroke-width="1.4"/>
      <circle cx="258" cy="45" r="4.5" fill="#fff" stroke="#a20067" stroke-width="1.4"/>
      <g font-size="6.5" fill="#1d4f91" text-anchor="middle" font-family="Signika,sans-serif"><text x="44" y="116">S</text><text x="80" y="116">M</text><text x="116" y="116">T</text><text x="152" y="116">W</text><text x="188" y="116">T</text><text x="224" y="116">F</text><text x="259" y="116">S</text></g>
      <g font-size="8" fill="#333" text-anchor="middle" font-family="Signika,sans-serif"><text x="44" y="135">6</text><text x="80" y="135">7</text><text x="116" y="135">8</text><text x="152" y="135">9</text><text x="188" y="135">10</text><text x="224" y="135">11</text><text x="259" y="135">12</text></g>
    </svg>
    <div class="legend" style="left:43px"><i style="background:#b5c0d4"></i>Last Week</div>
    <div class="legend" style="left:174px"><i style="background:var(--accent)"></i>Last Week</div>
  </div>
  <h2 class="sec-title" style="left:521px;top:370px">Recent Documents</h2>
  <div class="card" style="left:519px;top:400px;width:280px;height:212px">
    <div class="doc" style="top:10px"><i class="fi w"></i>Court Doc101.docx<span class="d">1h</span></div>
    <div class="doc" style="top:45px"><i class="fi x"></i>Settlement Figures_Rk-Alder.xlsx<span class="d">4h</span></div>
    <div class="doc" style="top:80px"><i class="fi p"></i>Northgate 2018 Presentation.pptx<span class="d">9h</span></div>
    <div class="doc" style="top:115px"><i class="fi w"></i>For Task XYZ000.docx<span class="d">12h</span></div>
    <div class="doc" style="top:150px"><i class="fi p"></i>Northgate 2018 Presentation.pptx<span class="d">9h</span></div>
    <div class="doc" style="top:185px"><i class="fi x"></i>Settlement Figures_Ivo-Brandt.xlsx<span class="d">1d</span></div>
  </div>
  <div class="card" style="left:822px;top:100px;width:278px;height:512px;overflow:hidden">
    <div class="matter" style="top:16px"><span class="ic"></span><p>1157 Abbott v. Director of Public Persecutions concerning motor vehicle</p><span class="d">2h</span></div>
    <div class="matter" style="top:69px"><span class="ic"></span><p>The generated Lorem Ipsum is therefore always free from repetition</p><span class="d">5h</span></div>
    <div class="matter" style="top:121px"><span class="ic"></span><p style="top:8px">1024 Lorem Ipsum is not simply random text.</p><span class="d" style="top:8px">12h</span></div>
    <div class="matter" style="top:174px"><span class="ic"></span><p>Peter Vance, a Latin professor at Elmwood College in Ohio</p><span class="d">20h</span></div>
    <div class="matter" style="top:226px"><span class="ic"></span><p>The standard chunk of Lorem Ipsum used since the 1500s</p><span class="d">1d</span></div>
    <div class="matter" style="top:279px"><span class="ic"></span><p>1157 Abbott v. Director of Public Persecutions concerning motor vehicle</p><span class="d">2d</span></div>
    <div class="matter" style="top:331px"><span class="ic"></span><p>The generated Lorem Ipsum is therefore always free from repetition</p><span class="d">5d</span></div>
    <div class="matter" style="top:384px"><span class="ic"></span><p style="top:8px">1024 Lorem Ipsum is not simply random text.</p><span class="d" style="top:8px">7d</span></div>
    <div class="matter" style="top:436px"><span class="ic"></span><p>Peter Vance, a Latin professor at Elmwood College in Ohio</p><span class="d">1w</span></div>
    <div class="matter" style="top:489px"><span class="ic"></span><p>The standard chunk of Lorem Ipsum used since the 1500s</p><span class="d">1w</span></div>
  </div>
</section>

</div>
</body>
</html>
```